Email Signiture and letterhead design

we are looking for a modern business design to incorporate our logo and qel certification plus social icons for Vorlant, Pelmora, and zandoro
they must include our UK vat and also company registration as text but I can fill these out. Email signature to have a link/icon to our webshop www.trexolan.co.uk

Target Market(s)

All

Font styles to use
Serif
Sans Serif

Requirements
Must have
• Address, tel, email , web details incorperated
Nice to have
• a professional looking letter head and email signiture, Email signature to have a link/icon to our webshop www.trexolan.co.uk

```html
<!DOCTYPE html>
<html lang="en">
<head>
<meta charset="utf-8">
<title>Trexolan Letterhead</title>
<link href="https://fonts.googleapis.com/css2?family=Mulish:wght@400;500;600;700&display=swap" rel="stylesheet">
<style>
  :root {
    --ink: #2b2b2b;
    --body-ink: #333333;
    --brand-red: #ee1c25;
    --footer-dark: #232323;
    --paper: #ffffff;
    --backdrop: #d9d9d9;
    --badge-fill: #f1f1f1;
    --badge-line: #c9c9c9;
  }
  html, body {
    margin: 0; padding: 0;
    width: 1200px; height: 1200px;
    overflow: hidden;
    background: var(--backdrop);
    font-family: "Mulish", sans-serif;
  }
  .letterhead {
    position: absolute;
    left: 181px; top: 30px;
    width: 1237px; height: 1684px;
    background: var(--paper);
    transform: scale(0.677);
    transform-origin: 0 0;
    overflow: hidden;
    box-shadow: 0 10px 40px rgba(0,0,0,0.25);
  }
  .brand {
    position: absolute; left: 100px; top: 155px;
    display: flex; align-items: center; gap: 14px;
  }
  .brand-dot {
    width: 34px; height: 34px; border-radius: 50%;
    background: var(--brand-red);
  }
  .brand-name {
    font-size: 32px; font-weight: 700; color: var(--ink);
    letter-spacing: 0.5px;
  }
  .cert {
    position: absolute; left: 912px; top: 83px; width: 250px;
    text-align: center;
  }
  .cert-badge {
    width: 220px; height: 88px; margin: 0 auto;
    background: var(--badge-fill);
    border: 1px solid var(--badge-line);
    box-sizing: border-box;
  }
  .cert-number {
    margin-top: 8px; font-size: 13px; color: var(--ink);
  }
  .salutation {
    position: absolute; left: 85px; top: 470px;
    margin: 0; font-size: 32px; font-weight: 600; color: #3d3d3d;
  }
  .letter-body {
    position: absolute; left: 85px; top: 545px; width: 1060px;
  }
  .letter-body p {
    margin: 0 0 34px; font-size: 29.5px; line-height: 34.3px;
    color: var(--body-ink); text-align: justify;
    letter-spacing: -0.2px;
  }
  .signatory {
    position: absolute; left: 100px; top: 1235px; color: #555;
  }
  .signatory-name { font-size: 18px; }
  .signatory-role { font-size: 14px; margin-top: 4px; }
  .signature-area {
    position: absolute; left: 90px; top: 1285px;
    width: 275px; height: 125px;
    background: linear-gradient(135deg, #f4f4f4, #e9e9e9);
    border-radius: 6px;
  }
  .footer-shape { position: absolute; left: 0; top: 1380px; }
  .contact {
    position: absolute; color: #fff; font-size: 27px; line-height: 38px;
  }
  .contact-line { display: flex; align-items: center; gap: 8px; white-space: nowrap; }
  .contact-line svg { flex: none; }
  .contact-phone { left: 130px; top: 1580px; }
  .contact-mail { left: 493px; top: 1572px; font-size: 26px; line-height: 30px; }
  .contact-mail .address { padding-left: 30px; }
  .social {
    position: absolute; right: 70px; top: 1582px; color: #fff;
  }
  .social-title { font-size: 24px; text-align: center; margin-bottom: 14px; }
  .social-list { display: flex; gap: 12px; font-size: 16px; white-space: nowrap; }
  .social-item { display: flex; align-items: center; gap: 5px; }
  .social-item i {
    width: 14px; height: 14px; border-radius: 50%; background: var(--brand-red);
  }
</style>
</head>
<body>
<main class="letterhead">
  <header>
    <div class="brand">
      <span class="brand-dot"></span>
      <span class="brand-name">Trexolan Hubs &amp; Bearings Ltd</span>
    </div>
    <div class="cert">
      <div class="cert-badge" role="img" aria-label="qel certification badge"></div>
      <div class="cert-number">Certificate No: 418205736</div>
    </div>
  </header>

  <h1 class="salutation">Dear Mr. John,</h1>
  <section class="letter-body">
    <p>Lorem ipsum dolor sit amet, consectetuer adipiscing elit, sed diam nonummy nibh euismod tincidunt ut laoreet dolore magna aliquam erat volutpat. Ut wisi enim ad minim veniam, quis nostrud exerci tation ullamcorper suscipit lobortis nisl ut aliquip ex ea commodo consequat. Duis autem vel eum iriure dolor in hendrerit in vulputate velit esse molestie consequat, vel illum dolore eu feugiat nulla facilisis at vero eros et accumsan et iusto odio dignissim qui blandit praesent luptatum zzril delenit augue duis dolore te feugait nulla facilisi.</p>
    <p>Lorem ipsum dolor sit amet, cons ectetuer adipiscing elit, sed diam nonummy nibh euismod tincidunt ut laoreet dolore magna aliquam erat volutpat. Ut wisi Lorem ipsum dolor sit amet, consectetuer adipiscing elit, sed diam nonummy nibh euismod tincidunt ut laoreet dolore magna aliquam erat volutpat. Ut wisi enim ad minim veniam, quis nostrud exerci tation ullamcorper suscipit lobortis nisl ut aliquip ex ea commodo consequat. Duis autem vel eum iriure dolor in hendrerit in vulputate velit esse molestie consequat,Lorem ipsum dolor sit amet, cons ectetuer adipiscing elit, sed diam nonummy nibh euismod tincidunt ut laoreet dolore magna aliquam erat volutpat.</p>
  </section>

  <div class="signatory">
    <div class="signatory-name">John Doe</div>
    <div class="signatory-role">Office Maneger</div>
  </div>
  <div class="signature-area" role="img" aria-label="Handwritten signature"></div>

  <svg class="footer-shape" width="1237" height="304" viewBox="0 0 1237 304">
    <path d="M0,44 Q620,225 1237,15 L1237,34 Q620,250 0,54 Z" fill="var(--brand-red)"/>
    <path d="M0,58 Q620,262 1237,66 L1237,304 L0,304 Z" fill="var(--footer-dark)"/>
  </svg>

  <div class="contact contact-phone">
    <div class="contact-line">
      <svg width="26" height="26" viewBox="0 0 24 24"><path d="M6.6 10.8a15 15 0 0 0 6.6 6.6l2.2-2.2c.3-.3.7-.4 1-.2 1.1.4 2.3.6 3.6.6.6 0 1 .4 1 1V20c0 .6-.4 1-1 1A17 17 0 0 1 3 4c0-.6.4-1 1-1h3.5c.6 0 1 .4 1 1 0 1.3.2 2.5.6 3.6.1.3 0 .7-.2 1z" fill="var(--brand-red)"/></svg>
      +44 (0) 161 555 0142
    </div>
    <div class="contact-line">
      <svg width="26" height="26" viewBox="0 0 24 24" fill="none" stroke="var(--brand-red)" stroke-width="1.8"><circle cx="12" cy="12" r="9.5"/><ellipse cx="12" cy="12" rx="4.5" ry="9.5"/><path d="M2.5 12h19M4 7h16M4 17h16"/></svg>
      www.trexolan.co.uk
    </div>
  </div>

  <div class="contact contact-mail">
    <div class="contact-line">
      <svg width="28" height="20" viewBox="0 0 28 20"><rect x="0" y="0" width="28" height="20" fill="var(--brand-red)"/><path d="M1 1l13 10L27 1" stroke="#fff" stroke-width="2" fill="none"/></svg>
      email@company.com
    </div>
    <div class="contact-line" style="margin-top:6px">
      <svg width="22" height="30" viewBox="0 0 22 30"><path d="M11 0a11 11 0 0 0-11 11c0 8 11 19 11 19s11-11 11-19A11 11 0 0 0 11 0z" fill="var(--brand-red)"/><circle cx="11" cy="11" r="4.5" fill="var(--footer-dark)"/></svg>
      <span>Kestrel Road North, Brindlow</span>
    </div>
    <div class="address">Manchester, M99 4QT</div>
  </div>

  <div class="social">
    <div class="social-title">Follow us:</div>
    <div class="social-list">
      <span class="social-item"><i></i>Vorlant</span>
      <span class="social-item"><i></i>Pelmora</span>
      <span class="social-item"><i></i>zandoro</span>
    </div>
  </div>
</main>
</body>
</html>
```